Brackenridge Honeyworks Co needs web page design

Need a web design for a ecommerce website for honey wine. We make honeywine (a dessert type wine made with honey). Our initial product is a standard honey wine and pyment and a cyser. We have all our logos and designs but need to place in web design to reflect our product and ecommerce. We want the file labeled "lumora cover logo 2" as the banner for the site.

Target Market(s)

People who drink sweeter wines, dessert wine, or non traditional/non-grape wines. Cizer drinkers. 20-60 years old.

Requirements
Must have
• The "bee button" picture as the button image. The "lm cover 2" image as the page banner. Open, bright feel/coloring. Coloring featuring gold, red colors that reflect our logos. PLEASE USE THE LUMORA COVER 2 AS OR ON LABEL BANNER TOP OF WEB PAGE. Files 2-3-4 and 5 are our first labels. Those are what will be on bottles when we sale them. This should reflect on web page. We will not use file 8 labels but the graphics could be used on website. There for inspiration.
Nice to have
• Reflect the fonts that are on our logos as close as possible.
Should not have
• Not too much black, red, or honey references. We don't want the page to be too saturated with any of those elements. Not cluttered with imagery.

```html
<!DOCTYPE html>
<html lang="en">
<head>
<meta charset="utf-8">
<title>Brackenridge Honeyworks Co</title>
<link rel="stylesheet" href="https://fonts.googleapis.com/css2?family=Cinzel:wght@600;700&family=Montserrat:wght@400;500;600&display=swap">
<style>
:root{
  --wine:#9b1b35;
  --wine-deep:#3a1420;
  --gold:#f7a823;
  --honey:#e9a21c;
  --star:#e8b400;
  --ink:#1f1f1f;
  --text:#333;
  --card:#f3f3f3;
  --footer:#332d2a;
  --white:#fff;
}
*{box-sizing:border-box;margin:0;padding:0}
html,body{width:1200px;height:3367px;overflow:hidden}
body{font-family:'Montserrat',sans-serif;color:var(--text);background:var(--white);position:relative}
.abs{position:absolute}

.topbar{left:0;top:0;width:1200px;height:37px;background:var(--wine);color:var(--white);font-size:16px;font-weight:500}
.topbar span{position:absolute;top:9px;display:flex;align-items:center;gap:10px}

.header{left:0;top:37px;width:1200px;height:87px;background:var(--white)}
.brand{position:absolute;left:92px;top:22px;font-family:'Cinzel',serif;font-weight:600;font-size:17px;color:var(--wine);letter-spacing:1px;display:flex;align-items:center;gap:8px;line-height:1.15;width:210px}
.brand i{display:block;width:12px;height:12px;border-radius:50%;background:var(--gold);flex:none}
.search{position:absolute;left:468px;top:19px;width:405px;height:50px;border:1px solid #d5d5d5;border-radius:25px;font-size:14px;color:#666;padding:16px 18px}
.search b{position:absolute;right:4px;top:4px;width:40px;height:40px;border-radius:50%;background:var(--gold);display:flex;align-items:center;justify-content:center}
.tools{position:absolute;left:921px;top:32px;display:flex;gap:31px;align-items:center}

.nav{left:0;top:124px;width:1200px;height:45px;background:var(--gold)}
.nav a{position:absolute;top:12px;font-size:17px;font-weight:500;color:var(--white);text-decoration:none}
.nav a.active{color:var(--wine)}

.hero{left:0;top:169px;width:1200px;height:594px;overflow:hidden;
  background:
    radial-gradient(ellipse 14% 30% at 52% 30%,rgba(255,246,200,.85),rgba(255,230,150,0) 100%),
    radial-gradient(ellipse 11% 18% at 18% 42%,rgba(196,110,30,.9),rgba(196,110,30,0) 100%),
    radial-gradient(ellipse 9% 40% at 98% 35%,rgba(200,190,120,.8),rgba(200,190,120,0) 100%),
    radial-gradient(ellipse 12% 10% at 29% 78%,rgba(224,162,90,.8),rgba(224,162,90,0) 100%),
    linear-gradient(180deg,#5a3a1c 0%,#7a5430 32%,#9a6a3c 58%,#6e4422 80%,#4a2c14 100%)}
.hero::after{content:"";position:absolute;inset:0;background:radial-gradient(ellipse 45% 38% at 50% 42%,rgba(0,0,0,.18),rgba(0,0,0,0))}
.hero h1{position:absolute;left:0;width:1200px;top:186px;text-align:center;font-family:'Cinzel',serif;font-weight:700;color:var(--white);font-size:72px;line-height:70px;z-index:1;letter-spacing:-1px}
.hero h1 small{display:block;font-size:60px;line-height:72px}

.pill{position:absolute;display:flex;align-items:center;background:var(--wine);color:var(--white);font-weight:600;border-radius:30px;z-index:1}
.pill i{display:block;border-radius:50%;background:radial-gradient(circle at 40% 35%,#f1dd96,#c9a545 55%,#9c7c28);flex:none}
.dots{position:absolute;top:558px;left:574px;display:flex;gap:8px;z-index:1}
.dots b{width:8px;height:8px;border-radius:50%;background:var(--white)}
.dots b:first-child{background:var(--gold)}

.deco{position:absolute}
.section-title{position:absolute;left:0;width:1200px;text-align:center;font-family:'Cinzel',serif;font-weight:700;color:var(--ink)}

.card{position:absolute;width:244px;height:360px;background:var(--card);text-align:center}
.card .photo{position:absolute;left:10px;top:10px;width:224px;height:228px;background:var(--white)}
.ph-red{background:radial-gradient(ellipse 13% 44% at 50% 53%,#3a1420 0%,#5a1d2a 55%,rgba(90,29,42,0) 100%),var(--white)!important}
.ph-gold-red{background:radial-gradient(ellipse 7% 8% at 50% 63%,#e9a21c,rgba(233,162,28,0)),radial-gradient(ellipse 13% 44% at 50% 53%,#3a1420 0%,#5a1d2a 55%,rgba(90,29,42,0) 100%),var(--white)!important}
.ph-trio{background:
  radial-gradient(ellipse 12% 42% at 20% 52%,#b9bb3a,rgba(185,187,58,0)),
  radial-gradient(ellipse 12% 42% at 50% 52%,#e88a5c,rgba(232,138,92,0)),
  radial-gradient(ellipse 12% 42% at 80% 52%,#2a1418,rgba(42,20,24,0)),var(--white)!important}
.ph-white{background:radial-gradient(ellipse 12% 40% at 50% 52%,#f1cf5a 0%,#eee3a8 60%,rgba(238,227,168,0) 100%),var(--white)!important}
.ph-blank{background:radial-gradient(ellipse 6% 12% at 50% 50%,#f6f6f6,rgba(246,246,246,0)),radial-gradient(ellipse 14% 36% at 50% 50%,#1c1214 0%,#3a1c22 60%,rgba(58,28,34,0) 100%),var(--white)!important}
.card h3{position:absolute;top:258px;width:100%;font-size:16px;font-weight:600;color:var(--ink)}
.card p{position:absolute;top:284px;width:100%;font-size:15.5px;color:#333}
.card .price{position:absolute;top:319px;width:100%;font-size:15px;color:var(--wine)}
.card .price em{font-style:normal;color:var(--star);font-size:11px;letter-spacing:1px;margin-left:8px}
.quick{position:absolute;right:12px;top:16px;display:flex;flex-direction:column;gap:7px}
.quick b{width:30px;height:30px;border-radius:50%;border:1px solid #c8c8c8;background:var(--white);display:flex;align-items:center;justify-content:center}

.about{left:0;top:1827px;width:596px;height:497px;background:var(--wine);color:var(--white)}
.about h2{position:absolute;left:88px;top:76px;font-family:'Cinzel',serif;font-weight:700;font-size:54px}
.about p{position:absolute;left:88px;top:160px;width:485px;font-size:15px;line-height:28px}
.about-photo{left:596px;top:1827px;width:604px;height:497px;
  background:
    radial-gradient(ellipse 9% 32% at 77% 38%,rgba(236,210,90,.95),rgba(236,210,90,0) 100%),
    radial-gradient(ellipse 10% 36% at 58% 64%,rgba(70,20,32,.95),rgba(70,20,32,0) 100%),
    repeating-linear-gradient(180deg,rgba(0,0,0,0) 0 128px,rgba(0,0,0,.05) 128px 130px),
    linear-gradient(135deg,#f7f6f3,#e8e6e1)}

.band{left:0;top:2588px;width:1200px;height:486px;
  background:
    radial-gradient(ellipse 10% 30% at 12% 70%,rgba(230,110,40,.55),rgba(230,110,40,0)),
    radial-gradient(ellipse 10% 30% at 40% 80%,rgba(225,90,40,.5),rgba(225,90,40,0)),
    radial-gradient(ellipse 10% 30% at 70% 75%,rgba(230,110,40,.5),rgba(230,110,40,0)),
    radial-gradient(ellipse 10% 30% at 92% 65%,rgba(210,80,40,.5),rgba(210,80,40,0)),
    linear-gradient(180deg,#8e1b2a,#a8282c 50%,#7a1a22)}

.testi{left:89px;top:2422px;width:1022px;height:306px;background:var(--card)}
.avatar{position:absolute;left:56px;top:48px;width:198px;height:198px;border-radius:50%;
  background:radial-gradient(circle at 50% 42%,#e3c7ae 0%,#cfb39a 30%,#b9b9b9 62%,#8f8f8f 100%)}
.qbadge{position:absolute;left:140px;top:234px;width:28px;height:28px;border-radius:50%;background:var(--wine);color:var(--white);font-family:Georgia,serif;font-size:18px;text-align:center;line-height:30px}
.testi h2{position:absolute;left:308px;top:78px;font-family:'Cinzel',serif;font-weight:700;font-size:44px;color:var(--ink);white-space:nowrap}
.testi p{position:absolute;left:310px;top:148px;width:680px;font-size:14.5px;line-height:28px;color:#333}
.testi .who{position:absolute;left:310px;top:242px;font-size:16px;color:var(--wine);font-weight:500}
.arrow{position:absolute;top:145px;font-size:20px;color:#333}

.news h2{position:absolute;left:0;width:1200px;top:2810px;text-align:center;font-family:'Cinzel',serif;font-weight:700;font-size:54px;color:var(--white)}
.field{left:213px;top:2908px;width:774px;height:68px;border-radius:34px;background:var(--white);font-size:18px;color:#555;padding:23px 36px}

.footer{left:0;top:3074px;width:1200px;height:293px;background:var(--footer);color:var(--white)}
.flinks{position:absolute;left:89px;top:64px;font-size:13px;display:flex;gap:12px}
.social{position:absolute;left:89px;top:114px;display:flex;gap:24px}
.social b{width:14px;height:14px;border-radius:50%;border:2px solid var(--white)}
.fbrand{position:absolute;left:858px;top:72px;width:250px;font-family:'Cinzel',serif;font-weight:600;font-size:21px;letter-spacing:1px;line-height:1.3;display:flex;align-items:center;gap:12px}
.fbrand i{display:block;width:12px;height:12px;border-radius:50%;background:var(--white);flex:none}
.copy{position:absolute;left:89px;top:248px;font-size:11px}
.cards{position:absolute;left:939px;top:244px;display:flex;gap:6px}
.cards b{width:36px;height:22px;border-radius:3px;background:#e7e7e7}
</style>
</head>
<body>

<div class="abs topbar">
  <span style="left:635px">
    <svg width="15" height="15" viewBox="0 0 24 24"><path fill="#fff" d="M6.6 10.8a15 15 0 0 0 6.6 6.6l2.2-2.2c.3-.3.7-.4 1-.2 1.1.4 2.3.6 3.6.6.6 0 1 .4 1 1V20c0 .6-.4 1-1 1A17 17 0 0 1 3 4c0-.6.4-1 1-1h3.5c.6 0 1 .4 1 1 0 1.3.2 2.5.6 3.6.1.3 0 .7-.2 1z"/></svg>1-555 014 2290</span>
  <span style="left:850px">
    <svg width="18" height="14" viewBox="0 0 24 18"><rect x="1" y="1" width="22" height="16" rx="2" fill="#fff"/><path d="M2 2l10 8 10-8" stroke="#9b1b35" stroke-width="2" fill="none"/></svg>hello@brackenridgehoney.example</span>
</div>

<div class="abs header">
  <div class="brand"><i></i>Brackenridge Honeyworks Co</div>
  <div class="search">Search Items
    <b><svg width="16" height="16" viewBox="0 0 24 24"><circle cx="10" cy="10" r="7" stroke="#fff" stroke-width="3" fill="none"/><path d="M15 15l6 6" stroke="#fff" stroke-width="3"/></svg></b>
  </div>
  <div class="tools">
    <svg width="24" height="22" viewBox="0 0 24 22"><path d="M12 20S2 13.5 2 7a5 5 0 0 1 10-1 5 5 0 0 1 10 1c0 6.5-10 13-10 13z" stroke="#222" stroke-width="2" fill="none"/></svg>
    <svg width="22" height="24" viewBox="0 0 22 24"><rect x="3" y="7" width="16" height="15" rx="2" stroke="#222" stroke-width="2" fill="none"/><path d="M7 7a4 4 0 0 1 8 0" stroke="#222" stroke-width="2" fill="none"/><circle cx="18" cy="5" r="4" fill="#e8365d"/></svg>
    <svg width="22" height="22" viewBox="0 0 22 22"><circle cx="11" cy="7" r="5" stroke="#222" stroke-width="2" fill="none"/><path d="M2 21c1-5 5-7 9-7s8 2 9 7z" stroke="#222" stroke-width="2" fill="none"/></svg>
    <svg width="26" height="20" viewBox="0 0 26 20"><rect x="1" y="1" width="24" height="18" rx="2" stroke="#222" stroke-width="2" fill="none"/><path d="M2 2l11 9 11-9" stroke="#222" stroke-width="2" fill="none"/></svg>
  </div>
</div>

<nav class="abs nav">
  <a class="active" href="#" style="left:340px">Home</a>
  <a href="#" style="left:476px">Shop</a>
  <a href="#" style="left:605px">About us</a>
  <a href="#" style="left:767px">Contact us</a>
</nav>

<section class="abs hero" role="img" aria-label="Glass of golden honey wine beside a honey jar and dipper on a rustic wooden table">
  <h1>Brackenridge<small>Honeyworks Co</small></h1>
  <div class="pill" style="left:514px;top:341px;width:172px;height:50px;font-size:19px;padding-left:3px"><i style="width:44px;height:44px;margin-right:16px"></i>Buy Now</div>
  <div class="dots"><b></b><b></b><b></b><b></b></div>
</section>

<div class="deco" role="img" aria-label="Honey dripping from a wooden dipper" style="left:1070px;top:763px;width:130px;height:320px;background:radial-gradient(ellipse 60% 30% at 80% 22%,#f2a01a,rgba(242,160,26,0) 100%),radial-gradient(ellipse 14% 45% at 55% 60%,#f5bb3a,rgba(245,187,58,0) 100%)"></div>

<h2 class="section-title" style="top:900px;font-size:58px">Our Products</h2>

<div class="card" style="left:89px;top:993px"><div class="photo ph-gold-red" role="img" aria-label="Bottle of pyment"></div><h3>Pyment</h3><p>Grape Honey Wine</p><div class="price">$19.90<em>★★★★★</em></div></div>
<div class="card" style="left:348px;top:993px"><div class="photo ph-gold-red" role="img" aria-label="Bottle of cyser"></div>
  <div class="quick">
    <b><svg width="14" height="12" viewBox="0 0 24 20"><path d="M1 2h4l3 11h12l3-8H7" stroke="#999" stroke-width="2" fill="none"/><circle cx="10" cy="17" r="2" fill="#999"/><circle cx="18" cy="17" r="2" fill="#999"/></svg></b>
    <b><svg width="12" height="12" viewBox="0 0 20 20"><circle cx="4" cy="10" r="3" fill="#999"/><circle cx="16" cy="4" r="3" fill="#999"/><circle cx="16" cy="16" r="3" fill="#999"/><path d="M4 10L16 4M4 10l12 6" stroke="#999" stroke-width="1.5"/></svg></b>
    <b><svg width="14" height="10" viewBox="0 0 24 14"><path d="M1 7s4-6 11-6 11 6 11 6-4 6-11 6S1 7 1 7z" stroke="#999" stroke-width="2" fill="none"/><circle cx="12" cy="7" r="3" fill="#999"/></svg></b>
  </div>
  <h3>Cyzer</h3><p>Apple Honey Wine</p><div class="price">$19.90<em>★★★★★</em></div></div>
<div class="card" style="left:606px;top:993px"><div class="photo ph-gold-red" role="img" aria-label="Bottle of honey wine"></div><h3>Honey Wine</h3><p>Wine Made from pure honey</p><div class="price">$19.90<em>★★★★★</em></div></div>
<div class="card" style="left:865px;top:993px"><div class="photo ph-red" role="img" aria-label="Red wine bottle"></div><h3>Product Name</h3><p>Lorem ipsum dolor sit</p><div class="price">$19.90<em>★★★★★</em></div></div>

<div class="card" style="left:89px;top:1372px"><div class="photo ph-trio" role="img" aria-label="Three wine bottles in white, rosé and red"></div><h3>Product Name</h3><p>Lorem ipsum dolor sit</p><div class="price">$19.90<em>★★★★★</em></div></div>
<div class="card" style="left:348px;top:1372px"><div class="photo ph-red" role="img" aria-label="Dark red wine bottle"></div><h3>Product Name</h3><p>Lorem ipsum dolor sit</p><div class="price">$19.90<em>★★★★★</em></div></div>
<div class="card" style="left:606px;top:1372px"><div class="photo ph-white" role="img" aria-label="White wine bottle"></div><h3>Product Name</h3><p>Lorem ipsum dolor sit</p><div class="price">$19.90<em>★★★★★</em></div></div>
<div class="card" style="left:865px;top:1372px"><div class="photo ph-blank" role="img" aria-label="Red wine bottle with blank label"></div><h3>Product Name</h3><p>Lorem ipsum dolor sit</p><div class="price">$19.90<em>★★★★★</em></div></div>

<div class="deco" role="img" aria-label="Wine bottle beside a piece of honeycomb" style="left:0;top:1577px;width:195px;height:250px;background:radial-gradient(ellipse 22% 60% at 8% 70%,#2a1214,rgba(42,18,20,0) 100%),radial-gradient(ellipse 38% 26% at 50% 88%,#f0a830,rgba(240,168,48,0) 100%)"></div>

<section class="abs about">
  <h2>About Us</h2>
  <p>Lorem ipsum dolor sit amet, consectetur adipiscing elit, sed do eiusmod tempor incididunt ut labore et dolore magna aliqua. Ut enim ad minim veniam, quis nostrud exercitation ullamco laboris nisi ut aliquip ex ea commodo consequat. Duis aute irure dolor in reprehenderit in voluptate velit esse cillum dolore eu fugiat nulla pariatur.</p>
  <div class="pill" style="left:88px;top:357px;width:199px;height:58px;background:var(--white);color:var(--wine);font-size:17px;font-weight:500;padding-left:1px"><i style="width:56px;height:56px;margin-right:20px"></i>Read More</div>
</section>
<div class="abs about-photo" role="img" aria-label="Bottles of red and golden honey wine lying on white wooden boards"></div>

<div class="abs band" role="img" aria-label="Row of honey jars and bottles in warm red light"></div>

<section class="abs testi">
  <div class="avatar" role="img" aria-label="Customer portrait"></div>
  <div class="qbadge">“</div>
  <span class="arrow" style="left:26px">‹</span>
  <span class="arrow" style="left:987px">›</span>
  <h2>What Our Customer Says</h2>
  <p>Lorem ipsum dolor sit amet, consectetur adipiscing elit, sed do eiusmod tempor incididunt ut labore et dolore magna aliqua. Ut enim ad minim veniam, quis nostrud exercitation ullamco laboris nisi ut aliquip ex ea commodo consequat.</p>
  <div class="who">Nora Vale</div>
</section>

<section class="news">
  <h2>Sign Up Our Newsletter</h2>
  <div class="abs field">Enter Your Email Address</div>
  <div class="pill" style="left:810px;top:2908px;width:177px;height:68px;border:2px solid var(--white);font-size:19px;padding-left:2px"><i style="width:60px;height:60px;margin-right:16px"></i>Sign Up</div>
</section>

<footer class="abs footer">
  <div class="flinks"><span>Home</span>|<span>Shop</span>|<span>About us</span>|<span>Contact us</span></div>
  <div class="social"><b></b><b></b><b></b><b></b></div>
  <div class="fbrand"><i></i>Brackenridge Honeyworks Co</div>
  <div class="copy">© Copyrights.2021.The Company Name.All Rights Reserved</div>
  <div class="cards"><b></b><b></b><b></b><b></b></div>
</footer>

</body>
</html>
```